Business Card Design Project

Hi,

We are a new modern sheet metal business and I require a business card for our sales reps.

The card should be double sided and standout in a crowd.

I have attached our logo and our website is www.plyform.com.au.

Please ask if you have any further questions
Updates

hi everyone, 

I'm wondering if we can try to lighten the cards mood.  Everyone is using black and I'm not sure how that would be accepted in real life.

Gordon

Reason: Still No receiving what I was hoping for.

Industry/Entity Type

Business

Requirements
Must have
• double sided

```html
<!DOCTYPE html>
<html lang="en">
<head>
<meta charset="utf-8">
<title>Keystone Sheetmetal – Business Card</title>
<link rel="stylesheet" href="https://fonts.googleapis.com/css2?family=Jost:ital,wght@0,400;0,600;0,700;1,400&display=swap">
<style>
  :root {
    --backdrop: #e4e5e7;
    --navy: #2d3d8c;
    --steel-dark: #4a4d53;
    --steel-light: #eef0f2;
    --steel-mid: #c3c6ca;
    --steel-shade: #a9adb2;
    --paper: #ffffff;
  }
  * { margin: 0; padding: 0; box-sizing: border-box; }
  html, body {
    width: 1200px;
    height: 787px;
    overflow: hidden;
    background: var(--backdrop);
    font-family: "Jost", "Futura", sans-serif;
  }
  .canvas {
    position: relative;
    width: 1200px;
    height: 787px;
  }
  .card {
    position: absolute;
    top: 224px;
    width: 540px;
    height: 338px;
    box-shadow: 0 6px 18px rgba(0, 0, 0, 0.18);
    overflow: hidden;
  }
  .brushed-steel {
    background:
      linear-gradient(180deg, rgba(255,255,255,0.35) 0%, rgba(255,255,255,0) 40%, rgba(0,0,0,0.06) 100%),
      linear-gradient(100deg, var(--steel-mid) 0%, var(--steel-light) 45%, var(--steel-mid) 75%, var(--steel-shade) 100%);
  }

  /* Front */
  .card-front { left: 40px; display: flex; background: var(--paper); }
  .front-strip {
    position: relative;
    width: 186px;
    height: 100%;
  }
  .strip-brand {
    position: absolute;
    left: 22px;
    bottom: 34px;
    color: var(--navy);
    font-weight: 700;
    line-height: 1;
  }
  .strip-brand .brand-word { display: block; font-size: 26px; letter-spacing: 0.5px; }
  .strip-brand .brand-sub { display: block; font-size: 11px; letter-spacing: 3px; margin-top: 3px; }
  .front-details {
    padding: 64px 0 0 20px;
    color: var(--navy);
  }
  .rep-name { font-size: 21px; font-weight: 700; line-height: 1.1; }
  .rep-role { font-size: 15px; font-style: italic; margin-top: 2px; }
  .contact-list {
    list-style: none;
    margin-top: 22px;
    font-size: 19px;
    line-height: 1.27;
  }
  .contact-list .label { display: inline-block; width: 88px; }
  .address-list {
    list-style: none;
    margin-top: 14px;
    font-size: 17px;
    line-height: 1.55;
  }

  /* Back */
  .card-back { left: 620px; }
  .back-brand {
    position: absolute;
    left: 0;
    right: 0;
    top: 74px;
    text-align: center;
    color: var(--steel-dark);
    font-weight: 700;
    line-height: 1;
  }
  .back-brand .brand-word { display: block; font-size: 84px; letter-spacing: 2px; }
  .back-brand .brand-sub { display: block; font-size: 24px; letter-spacing: 9px; margin-top: 10px; }
  .product-line {
    position: absolute;
    left: 0;
    right: 0;
    bottom: 52px;
    text-align: center;
    font-size: 21px;
    color: var(--steel-dark);
  }
  .product-line .divider { margin: 0 10px; }
</style>
</head>
<body>
<main class="canvas">
  <section class="card card-front" aria-label="Business card front">
    <div class="front-strip brushed-steel">
      <div class="strip-brand">
        <span class="brand-word">KEYSTONE</span>
        <span class="brand-sub">SHEETMETAL</span>
      </div>
    </div>
    <div class="front-details">
      <p class="rep-name">John Doe</p>
      <p class="rep-role">Sales Representative</p>
      <ul class="contact-list">
        <li><span class="label">Mobile</span>: 555 210 3391</li>
        <li><span class="label">Phone</span>: 3555 0142</li>
        <li><span class="label">Fax</span>: 3555 0188</li>
      </ul>
      <ul class="address-list">
        <li>28 Quartz Road Wacol Park Q 4076</li>
        <li>PO Box 87 Wacol Park Q 4076</li>
      </ul>
    </div>
  </section>

  <section class="card card-back brushed-steel" aria-label="Business card back">
    <div class="back-brand">
      <span class="brand-word">KEYSTONE</span>
      <span class="brand-sub">SHEETMETAL</span>
    </div>
    <p class="product-line">Flashings<span class="divider">|</span>Gutter<span class="divider">|</span>Rainwater Goods</p>
  </section>
</main>
</body>
</html>
```